Online Music Gear Store needs Business Cards

We need BC designs for our e-commerce for meetings and networking
we are an Online Store and we sell Audio and Music Equipment and Gear
we also provide EVENTUAL Audio and Music Production services but our core service is the Online Store: Selling Premium Brands

we are based in Tijuana and San Diego CA.
our brand/name is: Vellmoor

our name comes from the early tape machines that the Corvanes and many other early day artist used to record with to do their magnificent masterpieces.

Now in 2014 we can have Amazing Studio-Quality Multitrack sessions with a few pieces of Gear and an Slatepod... For example, you can only have your Pocketline and an Brisa Tandem to start recording using Loft Deck for Quorix.

If the best bands from the early days had to use million dollar recording studios with very expensive gear such as 4-track tape machines... now you can achieve better sounding results in your bedroom, using the gear we sell.

Thats what we try to Communicate with the Name:

That you... a young musician can start doing multitrack sessions using the Best Gear with the Latest Technology and compatible with Trelons, Quorix devices:

Example of the Premium Brands we sell are:
Brisa, ZQ Mediaworks

we want to communicate (even if we are an ecommerce and a startup) that we are Serious, and Very Elegant, Sophisticated and Minimal.

that we provide Complete solutions, the best gear... the best brands... that we also do our productions with the best gear, best brands and very important we are Pomeroy ONLY, Trelons Only

examples of the brands we sell are Kolbrandt, Brisa, ZQ Mediaworks, Rolf Ingham Instruments, Arc 9. Our focus is Music Technology.
we also use Cadence Max Q.

Our favorite colors are black, white, grey, silver, orange, blue, green, maybe bit of yellow.

No need to use all of them but you can combine. At the end you can use Color Theory to achieve assertive communication.

Target Market(s)

CEO's, VP's, VC's, Sales People, High Class executives...
Purchasing Departments, and Corporations.

Industry/Entity Type

E-Commerce

Requirements
Must have
• Should include:

1. Logo
2. website,
3. Managing Director Info:
4. Minimal and Elegant/Upper Class

feel free to suggest ideas, feel free to play around with logo and fonts as well... since we are not 100% happy with our logo...

must also show that we are Pomeroy and Trelon only in a way without being obvious or without showing Pomeroy Logo

we need to have at the end of the project the .AI
.PSD and any related designed file to edit in the future, logo, numbers, etc...

my info:

Tomas Emil Varga-Lindqvist
Vellmoor | Mexico City, Tijuana, San Diego,
Chatterbox | Peeplo | Zenbo+ | Clipwall | Snapframe ???? (what do you thing about this links ???) too much ???
Mobile: +5219987350418 | 0115219987350418
USA Number: 1-800-572-9183
VuCall & QuickNote: studio@vellmoor-example.mx
Talkwave: studiovellmoormx
Should not have
• it shouldn't use our real address, but should imply that we are in Mexico City, in Tijuana and San Diego CA.

Should not use the Pomeroy Logo (even if we are Pomeroy only)

should not have Robotix or PC/Panelix related designs.

```html
<!DOCTYPE html>
<html lang="en">
<head>
<meta charset="utf-8">
<title>Vellmoor — Business Card</title>
<link rel="stylesheet" href="https://fonts.googleapis.com/css2?family=Open+Sans:wght@400;600&display=swap">
<style>
  :root {
    --page-bg: #ffffff;
    --ink-dark: #3b3b3b;
    --ink-mid: #555555;
    --band-grey: #ececec;
    --card-dark-center: #4a4a4a;
    --card-dark-edge: #242222;
    --accent-lime: #b7cc1c;
    --white: #ffffff;
  }
  * { margin: 0; padding: 0; box-sizing: border-box; }
  html, body {
    width: 1128px;
    height: 1200px;
    overflow: hidden;
    background: var(--page-bg);
    font-family: "Open Sans", Arial, sans-serif;
  }
  .canvas {
    position: relative;
    width: 1128px;
    height: 1200px;
  }

  /* Front side */
  .card-front {
    position: absolute;
    left: 58px;
    top: 58px;
    width: 1023px;
    height: 512px;
    background: var(--white);
  }
  .card-front .band-top,
  .card-front .band-bottom {
    position: absolute;
    left: 0;
    width: 100%;
  }
  .card-front .band-top {
    top: 0;
    height: 66px;
    background: linear-gradient(to bottom, var(--band-grey), var(--white));
  }
  .card-front .band-bottom {
    bottom: 0;
    height: 58px;
    background: linear-gradient(to top, var(--band-grey), var(--white));
  }
  .brand-mark {
    position: absolute;
    display: flex;
    align-items: center;
    gap: 12px;
  }
  .brand-mark .mark-square {
    background: var(--accent-lime);
    flex: none;
  }
  .brand-mark .brand-name {
    font-weight: 600;
    line-height: 1;
    letter-spacing: -0.5px;
  }
  .card-front .brand-mark {
    left: 108px;
    top: 230px;
  }
  .card-front .mark-square { width: 22px; height: 22px; }
  .card-front .brand-name {
    font-size: 40px;
    color: var(--ink-dark);
  }

  .contact-block {
    position: absolute;
    left: 415px;
    top: 137px;
    color: var(--ink-dark);
  }
  .contact-block .person-name {
    font-size: 31px;
    font-weight: 600;
    letter-spacing: 0.8px;
    line-height: 38px;
  }
  .contact-block .person-role {
    font-size: 23px;
    font-weight: 400;
    letter-spacing: 0.6px;
    line-height: 30px;
  }
  .contact-block .contact-lines {
    list-style: none;
    margin-top: 17px;
    font-size: 16px;
    line-height: 25.5px;
    color: var(--ink-mid);
  }
  .contact-block .locations {
    margin-top: 18px;
    font-size: 19px;
    color: var(--ink-dark);
    word-spacing: 2px;
  }
  .contact-block .locations .divider { margin: 0 10px; }

  /* Back side */
  .card-back {
    position: absolute;
    left: 59px;
    top: 641px;
    width: 1022px;
    height: 512px;
    background: radial-gradient(circle at 50% 45%, var(--card-dark-center) 0%, #363535 40%, var(--card-dark-edge) 85%);
    display: flex;
    align-items: center;
    justify-content: center;
  }
  .card-back .brand-mark {
    position: static;
    gap: 22px;
  }
  .card-back .mark-square { width: 44px; height: 44px; }
  .card-back .brand-name {
    font-size: 104px;
    color: var(--white);
    letter-spacing: -1px;
  }
</style>
</head>
<body>
<main class="canvas">

  <section class="card-front" aria-label="Business card front">
    <div class="band-top"></div>
    <div class="band-bottom"></div>

    <div class="brand-mark">
      <span class="mark-square"></span>
      <span class="brand-name">Vellmoor.mx</span>
    </div>

    <div class="contact-block">
      <h1 class="person-name">TOMAS EMIL VARGA-LINDQVIST</h1>
      <p class="person-role">MANAGING DIRECTOR</p>
      <ul class="contact-lines">
        <li>M &gt; +5219987350418 &nbsp;&gt;&nbsp; 0115219 987350 418</li>
        <li>USA Number &gt; 1-800-572-9183</li>
        <li>Talkwave &gt; studiovellmoormx</li>
        <li>VuCall &amp; QuickNote &gt; studio@vellmoor-example.mx</li>
      </ul>
      <p class="locations">Mexico City<span class="divider">|</span>Tijuana<span class="divider">|</span>San Diego</p>
    </div>
  </section>

  <section class="card-back" aria-label="Business card back">
    <div class="brand-mark">
      <span class="mark-square"></span>
      <span class="brand-name">Vellmoor</span>
    </div>
  </section>

</main>
</body>
</html>
```